Business Card Design Project

Business Card design based on logo.

I need business card, letterhead, envelope, and if possible, Powerpoint slide template.

On front of business card: Just logo- and  my name and title:  Rosalind Pekar, Principal

On reverse-logo and the rest of the contact info:

4857 Orchard Lane
Davis, CA 95618
650-381-2276
rp@brindlestudyworks.example

On letterhead-Just logo at top, at bottom  the rest-very small along the bottom

On PPT slide-just the logo.

I also want to try a few other colors-I like lime/dark grey (not black) but would like to try Sienna, maybe also indigo or bright blue-green.

I forgot to add-

On the business card-switch to vertical on reverse side and put:

Reverse side-switch to vertical and list:

Rosalind Pekar
Principal
Brindle Study Works, LLC

650-381-2276

4857 Orchard Lane
Davis, CA 95618

Rosalind Pekar
Principal

650-381-2276

4857 Orchard Lane
Davis, CA 95618

I have another project at the same time-for Stationery. Feel free to submit to that one also.

That one includes letterhead, envelope, PPT slide, folder cover sheet-RP

Industry/Entity Type

Business

Requirements
Must have
• Must use logo-preferably lime green version-with gray, not black or just 2-tone -logo on colored background.

```html
<!DOCTYPE html>
<html lang="en">
<head>
<meta charset="utf-8">
<title>Brindle Study Works – Business Card</title>
<link rel="stylesheet" href="https://fonts.googleapis.com/css2?family=Lato:wght@400;700&display=swap">
<style>
  :root {
    --lime: #8dc63f;
    --graphite: #4a4a4c;
    --slate: #5c5c5e;
    --rule: #9a9a9a;
    --paper: #ffffff;
    --backdrop: #e6e9ea;
  }
  * { box-sizing: border-box; margin: 0; padding: 0; }
  html, body {
    width: 1200px;
    height: 960px;
    overflow: hidden;
    background: var(--backdrop);
    font-family: "Lato", Arial, sans-serif;
  }
  .sheet {
    position: relative;
    width: 1200px;
    height: 960px;
  }
  .card {
    position: absolute;
    background: var(--paper);
    box-shadow: 0 6px 18px rgba(0,0,0,0.12);
  }

  /* front: horizontal, brand only */
  .card--front {
    left: 90px;
    top: 320px;
    width: 560px;
    height: 320px;
  }

  /* reverse: vertical, contact details */
  .card--reverse {
    left: 770px;
    top: 200px;
    width: 320px;
    height: 560px;
    padding: 48px 34px 40px;
    display: flex;
    flex-direction: column;
  }

  .brand-mark {
    display: flex;
    align-items: center;
    gap: 10px;
  }
  .brand-mark__square {
    background: var(--lime);
    flex: none;
  }
  .brand-mark__name {
    font-weight: 700;
    color: var(--graphite);
    text-transform: uppercase;
    line-height: 1.1;
    white-space: nowrap;
  }
  .card--front .brand-mark {
    position: absolute;
    inset: 0;
    justify-content: center;
  }
  .card--front .brand-mark__square { width: 26px; height: 26px; }
  .card--front .brand-mark__name { font-size: 32px; letter-spacing: 3px; }

  .card--reverse .brand-mark__square { width: 14px; height: 14px; }
  .card--reverse .brand-mark__name { font-size: 16px; letter-spacing: 1.5px; }

  .holder { margin-top: 56px; }
  .holder__name {
    font-size: 25px;
    letter-spacing: 0.5px;
    color: var(--slate);
    text-transform: uppercase;
    white-space: nowrap;
  }
  .holder__first { color: var(--lime); }
  .holder__title {
    margin-top: 4px;
    font-size: 17px;
    letter-spacing: 1.6px;
    color: var(--slate);
    text-transform: uppercase;
  }
  .holder__company {
    margin-top: 10px;
    font-size: 14px;
    letter-spacing: 0.3px;
    color: var(--slate);
  }

  .contact-list {
    margin-top: auto;
    list-style: none;
  }
  .contact-list li {
    display: flex;
    align-items: center;
    height: 26px;
    font-size: 14px;
    color: var(--slate);
    letter-spacing: 0.3px;
    white-space: nowrap;
  }
  .contact-list svg {
    width: 14px;
    height: 14px;
    margin-right: 14px;
    fill: var(--lime);
    flex: none;
  }
  .contact-rule {
    margin-top: 14px;
    width: 100%;
    height: 1px;
    background: var(--rule);
  }
  .address {
    margin-top: 10px;
    font-size: 12.5px;
    line-height: 1.5;
    letter-spacing: 0.3px;
    color: var(--slate);
    text-transform: uppercase;
  }
</style>
</head>
<body>
<main class="sheet">
  <section class="card card--front" aria-label="Business card, front">
    <div class="brand-mark">
      <span class="brand-mark__square"></span>
      <span class="brand-mark__name">Brindle Study Works</span>
    </div>
  </section>

  <section class="card card--reverse" aria-label="Business card, reverse">
    <div class="brand-mark">
      <span class="brand-mark__square"></span>
      <span class="brand-mark__name">Brindle Study Works</span>
    </div>

    <div class="holder">
      <p class="holder__name"><span class="holder__first">Rosalind</span> Pekar</p>
      <p class="holder__title">Principal</p>
      <p class="holder__company">Brindle Study Works, LLC</p>
    </div>

    <ul class="contact-list">
      <li>
        <svg viewBox="0 0 16 16" aria-hidden="true"><path d="M1 5c0-2 3-3 7-3s7 1 7 3v1h-3V5c0-.6-1.6-1-4-1S4 4.4 4 5v1H1zM4 7h8l2 7H2zM8 8.5a2 2 0 1 0 0 4a2 2 0 0 0 0-4z"/></svg>
        650-381-2276
      </li>
      <li>
        <svg viewBox="0 0 16 16" aria-hidden="true"><path d="M1 3h14v10H1zM2.5 4.5 8 9l5.5-4.5v7h-11z" fill-rule="evenodd"/></svg>
        rp@brindlestudyworks.example
      </li>
      <li>
        <svg viewBox="0 0 16 16" aria-hidden="true"><circle cx="8" cy="8" r="7"/><path d="M5 3c2 1 1 3 3 3s1 3-1 3-2 3-1 4M10 10c1-1 3 0 3-1" stroke="#fff" stroke-width="1.2" fill="none"/></svg>
        www.brindlestudyworks.example
      </li>
    </ul>
    <div class="contact-rule"></div>
    <p class="address">4857 Orchard Lane<br>Davis, CA 95618</p>
  </section>
</main>
</body>
</html>
```